Design a Form to Match a Web Page Design

I need to you a proposal to get this form (3 pages) https://www.quarrybirchhall.com/eforms/analise-de-financiamento-e-rentabilidade-copy/35/ and match with the design concept of my home page https://www.quarrybirchhall.com/

```html
<!DOCTYPE html>
<html lang="en">
<head>
<meta charset="utf-8">
<title>Financing and Profitability Analysis Form</title>
<link href="https://fonts.googleapis.com/css2?family=Poppins:wght@500;600;700&family=Open+Sans:wght@400;600&display=swap" rel="stylesheet">
<style>
:root{
  --bg:#f2f2f2;
  --header:#14a0be;
  --banner:#d4204b;
  --teal:#17939c;
  --accent:#f47c22;
  --ink:#3f3f3f;
  --muted:#6a6a6a;
  --line:#dcdcdc;
  --track:#d9d9d9;
  --knob:#1596b3;
  --red:#d4204b;
}
*{margin:0;padding:0;box-sizing:border-box}
html,body{width:1200px;height:1155px;overflow:hidden;background:var(--bg)}
.stage{position:absolute;left:0;top:0;width:1960px;height:1887px;transform:scale(.61225);transform-origin:0 0;font-family:"Open Sans",sans-serif;color:var(--ink)}
.panel{position:absolute;background:#fff;border-radius:4px;overflow:hidden}
.steps-bar{position:absolute;left:0;right:0;top:0;height:90px;background:var(--header)}
.banner{position:absolute;left:0;right:0;top:90px;height:115px;background:var(--banner);color:#fff;text-align:center}
.banner h1{font-family:"Poppins",sans-serif;font-weight:700;font-size:33px;letter-spacing:.3px;margin-top:22px;line-height:40px}
.banner p{font-size:20px;margin-top:4px}
.dot{position:absolute;width:12px;height:12px;border:2.5px solid #fff;border-radius:50%;top:21px}
.dash{position:absolute;top:26px;height:0;border-top:2px dotted rgba(255,255,255,.7)}
.step{position:absolute;top:40px;width:160px;margin-left:-80px;text-align:center;font-family:"Poppins",sans-serif;font-weight:700;font-size:22px;color:rgba(255,255,255,.55)}
.step.on{color:#fff}
.card{position:absolute;border:2px solid var(--line);background:#fff}
.t{position:absolute;white-space:nowrap;line-height:1}
.lbl{font-size:17px;color:var(--ink)}
.sm{font-size:14px;color:var(--ink)}
.strong{font-weight:600;color:#2c2c2c}
.red{color:var(--red)}
.big{font-size:24px;color:var(--teal)}
.ttl{font-family:"Poppins",sans-serif;font-weight:600;font-size:24px;color:var(--muted)}
.ttl.s20{font-size:20px;line-height:25px}
.track{position:absolute;height:3px;background:var(--track)}
.knob{position:absolute;width:16px;height:16px;border:3.5px solid var(--knob);border-radius:50%;background:#fff}
.chev{position:absolute;width:22px;height:13px}
.btn{position:absolute;height:47px;width:173px;border-radius:24px;color:#fff;font-family:"Poppins",sans-serif;font-weight:600;font-size:18px;line-height:47px;text-align:center}
.btn.prev{background:var(--teal)}
.btn.next{background:var(--accent)}
.cal{position:absolute;width:15px;height:15px}
</style>
</head>
<body>
<div class="stage">

<!-- Step 1 : Property Financing -->
<section class="panel" style="left:57px;top:55px;width:889px;height:850px">
  <div class="steps-bar">
    <span class="dot" style="left:227px"></span><span class="dash" style="left:244px;width:183px"></span>
    <span class="dot" style="left:432px"></span><span class="dash" style="left:449px;width:184px"></span>
    <span class="dot" style="left:634px"></span>
    <span class="step on" style="left:235px">STEP 01</span>
    <span class="step" style="left:442px">STEP 02</span>
    <span class="step" style="left:641px">STEP 03</span>
  </div>
  <div class="banner"><h1>PROPERTY FINANCING</h1><p>Todos os valores apresentados em estão em Dólares Americanos</p></div>
</section>
<div class="card" style="left:74px;top:286px;width:855px;height:485px"></div>
<span class="t ttl" style="left:103px;top:311px">Property Financing</span>
<span class="t lbl" style="left:105px;top:389px">Property Value</span>
<span class="t lbl red" style="left:103px;top:426px">$</span>
<div class="track" style="left:130px;top:434px;width:320px"></div><div class="knob" style="left:122px;top:427px"></div>
<span class="t lbl" style="left:456px;top:427px">0</span>
<span class="t lbl" style="left:105px;top:488px">Entry (%) *</span>
<span class="t lbl red" style="left:103px;top:522px">30</span>
<div class="track" style="left:137px;top:530px;width:319px"></div><div class="knob" style="left:129px;top:523px"></div>
<span class="t lbl" style="left:104px;top:567px">Term (Years) *</span>
<span class="t lbl red" style="left:104px;top:602px">30</span>
<div class="track" style="left:138px;top:609px;width:319px"></div><div class="knob" style="left:130px;top:603px"></div>
<span class="t lbl" style="left:104px;top:657px">Input Value</span>
<span class="t lbl" style="right:1490px;top:657px">$ 0.00</span>
<span class="t lbl" style="left:104px;top:706px">Funded Amount</span>
<span class="t lbl" style="right:1490px;top:706px">$ 0.00</span>
<span class="t lbl" style="left:507px;top:406px">Financing Rate (Annual)</span>
<span class="t lbl red" style="left:507px;top:443px">%</span>
<div class="track" style="left:536px;top:451px;width:317px"></div><div class="knob" style="left:528px;top:444px"></div>
<span class="t lbl" style="left:861px;top:443px">5.75</span>
<span class="t lbl" style="left:507px;top:499px">Installment Value</span>
<span class="t big" style="right:1062px;top:496px">$0.00</span>
<span class="t lbl" style="left:511px;top:569px">Safe</span>
<span class="t lbl" style="right:1070px;top:569px">$ 0.00</span>
<span class="t lbl" style="left:511px;top:619px">Property Fees</span>
<span class="t lbl" style="right:1070px;top:619px">$ 0.00</span>
<span class="t lbl strong" style="left:516px;top:687px">Total Monthly Value</span>
<span class="t big" style="right:1067px;top:675px">$0.00</span>
<span class="btn prev" style="left:339px;top:801px">Previous</span>
<span class="btn next" style="left:528px;top:801px">Next</span>

<!-- Step 2 : Deed and Furniture Costs -->
<section class="panel" style="left:57px;top:1008px;width:889px;height:802px">
  <div class="steps-bar">
    <span class="dot" style="left:220px"></span><span class="dash" style="left:245px;width:180px"></span>
    <span class="dot" style="left:425px"></span><span class="dash" style="left:449px;width:184px"></span>
    <span class="dot" style="left:634px"></span>
    <span class="step" style="left:228px">STEP 01</span>
    <span class="step on" style="left:435px">STEP 02</span>
    <span class="step" style="left:641px">STEP 03</span>
  </div>
  <div class="banner"><h1>DEED AND FURNITURE COSTS</h1><p>Todos os valores apresentados em estão em Dólares Americanos</p></div>
</section>
<div class="card" style="left:81px;top:1236px;width:414px;height:443px"></div>
<div class="card" style="left:510px;top:1236px;width:420px;height:172px"></div>
<div class="card" style="left:510px;top:1421px;width:420px;height:258px"></div>
<span class="t ttl" style="left:112px;top:1273px">Expenses in Deed</span>
<svg class="chev" style="left:435px;top:1281px" viewBox="0 0 22 13"><polyline points="2,11 11,2 20,11" fill="none" stroke="#9a9a9a" stroke-width="2"/></svg>
<span class="t lbl" style="left:110px;top:1342px">Bank Costs / Financing</span>
<span class="t lbl" style="right:1497px;top:1342px">$0.00</span>
<span class="t lbl" style="left:110px;top:1392px">Expenses with Notary / Escrow</span>
<span class="t lbl" style="right:1494px;top:1396px">$0.00</span>
<span class="t lbl" style="left:110px;top:1441px">Incentive</span>
<span class="t lbl" style="right:1496px;top:1457px">-5000</span>
<span class="t lbl red" style="left:108px;top:1475px">$</span>
<div class="track" style="left:130px;top:1483px;width:332px"></div><div class="knob" style="left:122px;top:1476px"></div>
<span class="t lbl" style="left:109px;top:1520px">Fees and Licenses</span>
<span class="t lbl" style="right:1494px;top:1517px">$1,330.00</span>
<span class="t lbl red" style="left:109px;top:1555px">30</span>
<span class="t lbl" style="left:109px;top:1610px">Total Closing</span>
<span class="t big" style="right:1490px;top:1605px">$&nbsp; -3,670.00</span>
<span class="t ttl" style="left:534px;top:1272px">Property Furniture</span>
<svg class="chev" style="left:874px;top:1280px" viewBox="0 0 22 13"><polyline points="2,11 11,2 20,11" fill="none" stroke="#9a9a9a" stroke-width="2"/></svg>
<span class="t lbl" style="left:534px;top:1337px">Approximate Furniture Cost</span>
<span class="t big" style="right:1063px;top:1334px">$ 0.00</span>
<span class="t ttl" style="left:534px;top:1437px">Total investment</span>
<svg class="chev" style="left:874px;top:1449px" viewBox="0 0 22 13"><polyline points="2,11 11,2 20,11" fill="none" stroke="#9a9a9a" stroke-width="2"/></svg>
<span class="t lbl" style="left:533px;top:1502px">Initial investment</span>
<span class="t big" style="right:1060px;top:1495px">$&nbsp; -3,670.00</span>
<span class="btn prev" style="left:331px;top:1721px">Previous</span>
<span class="btn next" style="left:520px;top:1721px">Next</span>

<!-- Step 3 : Deed and Furniture Costs / results -->
<section class="panel" style="left:1018px;top:56px;width:889px;height:1626px">
  <div class="steps-bar">
    <span class="dot" style="left:220px"></span><span class="dash" style="left:245px;width:180px"></span>
    <span class="dot" style="left:425px"></span><span class="dash" style="left:449px;width:184px"></span>
    <span class="dot" style="left:634px"></span>
    <span class="step" style="left:228px">STEP 01</span>
    <span class="step" style="left:435px">STEP 02</span>
    <span class="step on" style="left:641px">STEP 03</span>
  </div>
  <div class="banner"><h1>DEED AND FURNITURE COSTS</h1><p>Todos os valores apresentados em estão em Dólares Americanos</p></div>
</section>
<div class="card" style="left:1043px;top:285px;width:415px;height:431px"></div>
<div class="card" style="left:1043px;top:727px;width:415px;height:215px"></div>
<div class="card" style="left:1470px;top:285px;width:421px;height:657px"></div>
<div class="card" style="left:1044px;top:956px;width:847px;height:466px"></div>
<div class="card" style="left:1046px;top:1433px;width:843px;height:118px"></div>

<span class="t ttl" style="left:1072px;top:315px">Recipe</span>
<svg class="chev" style="left:1397px;top:317px" viewBox="0 0 22 13"><polyline points="2,11 11,2 20,11" fill="none" stroke="#9a9a9a" stroke-width="2"/></svg>
<span class="t lbl" style="left:1072px;top:374px">Daily Rate</span>
<span class="t lbl red" style="left:1072px;top:403px">$</span>
<div class="track" style="left:1099px;top:411px;width:287px"></div><div class="knob" style="left:1091px;top:404px"></div>
<span class="t lbl" style="left:1403px;top:404px">0</span>
<span class="t lbl" style="left:1072px;top:447px">Annual Occupancy Rate (%)</span>
<span class="t lbl red" style="left:1072px;top:484px">73</span>
<div class="track" style="left:1097px;top:491px;width:289px"></div><div class="knob" style="left:1271px;top:485px"></div>
<span class="t lbl" style="left:1396px;top:483px">73%</span>
<span class="t lbl" style="left:1069px;top:533px">Days of busy year</span>
<svg class="cal" style="left:1384px;top:535px" viewBox="0 0 15 15"><rect x="1" y="2.5" width="13" height="11.5" rx="1" fill="none" stroke="#6f9eb0" stroke-width="1.4"/><line x1="1" y1="6" x2="14" y2="6" stroke="#6f9eb0" stroke-width="1.4"/><line x1="4.5" y1="1" x2="4.5" y2="4" stroke="#6f9eb0" stroke-width="1.4"/><line x1="10.5" y1="1" x2="10.5" y2="4" stroke="#6f9eb0" stroke-width="1.4"/></svg>
<span class="t lbl" style="left:1402px;top:533px">266</span>
<span class="t lbl" style="left:1069px;top:582px">Vacant year days</span>
<svg class="cal" style="left:1384px;top:582px" viewBox="0 0 15 15"><rect x="1" y="2.5" width="13" height="11.5" rx="1" fill="none" stroke="#6f9eb0" stroke-width="1.4"/><line x1="1" y1="6" x2="14" y2="6" stroke="#6f9eb0" stroke-width="1.4"/><line x1="4.5" y1="1" x2="4.5" y2="4" stroke="#6f9eb0" stroke-width="1.4"/><line x1="10.5" y1="1" x2="10.5" y2="4" stroke="#6f9eb0" stroke-width="1.4"/></svg>
<span class="t lbl" style="left:1402px;top:580px">99</span>
<span class="t lbl strong" style="left:1071px;top:647px">Gross Revenue</span>
<span class="t big" style="right:526px;top:643px">$ 0.00</span>

<span class="t ttl" style="left:1072px;top:757px;font-size:26px">Adm Commission (20%)</span>
<svg class="chev" style="left:1397px;top:761px" viewBox="0 0 22 13"><polyline points="2,11 11,2 20,11" fill="none" stroke="#9a9a9a" stroke-width="2"/></svg>
<span class="t lbl" style="left:1072px;top:819px">Adm.</span>
<span class="t lbl" style="right:535px;top:821px">$0.00</span>
<span class="t sm" style="left:1072px;top:848px">Commission 20% (Under Gross Revenue)</span>
<span class="t lbl strong" style="left:1073px;top:882px">Net Revenue</span>
<span class="t big" style="right:535px;top:877px">$ 0.00</span>

<span class="t ttl s20" style="left:1493px;top:310px">Amortization Financing<br>and Amount Invested</span>
<svg class="chev" style="left:1835px;top:328px" viewBox="0 0 22 13"><polyline points="2,11 11,2 20,11" fill="none" stroke="#9a9a9a" stroke-width="2"/></svg>
<span class="t lbl" style="left:1493px;top:403px;line-height:25px;margin-top:-4px">Financing Portion<br>(12 months)</span>
<span class="t lbl" style="right:99px;top:405px">$0.00</span>
<span class="t lbl" style="left:1492px;top:481px">Initial investment</span>
<span class="t lbl" style="right:89px;top:483px">$3,670.00</span>
<span class="t lbl" style="left:1493px;top:542px;line-height:25px">ROI (Profitability<br>/ Investment)</span>
<span class="t big" style="right:85px;top:541px">327.52 %</span>
<span class="t lbl" style="left:1492px;top:623px">Debt amortization</span>
<span class="t big" style="right:116px;top:618px">$ 0.00</span>
<span class="t lbl" style="left:1493px;top:696px">Amortization ROI</span>
<span class="t big" style="right:84px;top:691px">327.52 %</span>

<span class="t ttl s20" style="left:1072px;top:989px">Fixed Property Expenses</span>
<svg class="chev" style="left:1398px;top:990px" viewBox="0 0 22 13"><polyline points="2,11 11,2 20,11" fill="none" stroke="#9a9a9a" stroke-width="2"/></svg>
<span class="t lbl" style="left:1072px;top:1027px">HOA ((Owners Association Fee) 12 months)</span>
<span class="t lbl red" style="left:1079px;top:1056px">$</span>
<span class="t lbl" style="right:548px;top:1056px">4200</span>
<div class="track" style="left:1084px;top:1082px;width:332px"></div><div class="knob" style="left:1076px;top:1076px"></div>
<span class="t lbl" style="left:1073px;top:1113px">Adm Rate + Licenses (12 months)</span>
<span class="t lbl red" style="left:1076px;top:1141px">$</span>
<span class="t lbl" style="right:551px;top:1141px">1800</span>
<div class="track" style="left:1081px;top:1167px;width:332px"></div><div class="knob" style="left:1073px;top:1160px"></div>
<span class="t lbl" style="left:1073px;top:1202px">Swimming Pool (12 months)</span>
<span class="t lbl red" style="left:1076px;top:1230px">$</span>
<span class="t lbl" style="right:560px;top:1230px">960</span>
<div class="track" style="left:1082px;top:1256px;width:332px"></div><div class="knob" style="left:1074px;top:1250px"></div>
<span class="t lbl" style="left:1075px;top:1296px">Light / Water / Gas (12 months)</span>
<span class="t lbl red" style="left:1078px;top:1324px">$</span>
<span class="t lbl" style="right:548px;top:1324px">3480</span>
<div class="track" style="left:1083px;top:1351px;width:333px"></div><div class="knob" style="left:1075px;top:1344px"></div>
<span class="t lbl" style="left:1518px;top:1063px">Maintenance (12 months)</span>
<span class="t lbl red" style="left:1521px;top:1091px">$</span>
<span class="t lbl" style="right:106px;top:1091px">1200</span>
<div class="track" style="left:1526px;top:1117px;width:332px"></div><div class="knob" style="left:1518px;top:1111px"></div>
<span class="t lbl" style="left:1520px;top:1157px">Accounting (12 months)</span>
<span class="t lbl red" style="left:1523px;top:1185px">$</span>
<span class="t lbl" style="right:113px;top:1185px">380</span>
<div class="track" style="left:1528px;top:1212px;width:332px"></div><div class="knob" style="left:1520px;top:1205px"></div>
<span class="t lbl" style="left:1514px;top:1252px;line-height:21px">Fixed Property<br>Expenses (12 months)</span>
<span class="t big" style="right:102px;top:1257px">$ -12,020.00</span>
<span class="t lbl" style="left:1514px;top:1338px">Profitability</span>
<span class="t big" style="right:102px;top:1325px">$ -12,020.00</span>

<span class="t ttl s20" style="left:1070px;top:1463px">Net Balance after paying the<br>financing installments</span>
<svg class="chev" style="left:1387px;top:1472px" viewBox="0 0 22 13"><polyline points="2,11 11,2 20,11" fill="none" stroke="#9a9a9a" stroke-width="2"/></svg>
<span class="t lbl" style="left:1495px;top:1465px">Final Net Balance</span>
<span class="t big" style="right:98px;top:1463px">$ -12,020.00</span>
<span class="btn prev" style="left:1287px;top:1575px">Previous</span>
<span class="btn next" style="left:1476px;top:1575px">Next</span>

</div>
</body>
</html>
```